Do i have coronavirus, flue or cold?

Using information from QRV and government agencies we want to make a easy to read infographic helping patients see if they have coronavirus, the flu or a cold. Using a flow diagram or whatever you think will make it easy to read and digest for the average lamen.

Information is in the word document and in the chart.

We are www.tovipharm.co.uk attached is our brand guidelines, we will be putting this infographic on our website and email/sms it to all of our 300,000 patients.

```html
<!DOCTYPE html>
<html lang="en">
<head>
<meta charset="utf-8">
<title>Do i have coronavirus, flu or cold?</title>
<link rel="stylesheet" href="https://fonts.googleapis.com/css2?family=Catamaran:wght@400;500;700;800;900&display=swap">
<style>
  :root {
    --brand-blue: #3434b9;
    --accent-orange: #f45d22;
    --soft-blue: #6b8cf0;
    --pale-blue: #e9eef6;
    --rule: #9a9ad4;
    --panel-rule: #8c8cd6;
    --white: #ffffff;
  }
  * { margin: 0; padding: 0; box-sizing: border-box; }
  html, body { width: 1200px; height: 2238px; overflow: hidden; background: var(--white); }
  body { font-family: "Catamaran", sans-serif; color: var(--brand-blue); }
  .infographic { position: relative; width: 1200px; height: 2238px; background: var(--white); overflow: hidden; }

  .accent { position: absolute; }
  .accent--left-blue { left: 0; top: 0; width: 55px; height: 294px; background: var(--soft-blue); }
  .accent--left-orange { left: 0; top: 250px; width: 27px; height: 225px; background: var(--accent-orange); }
  .accent--right-orange { left: 1150px; top: 0; width: 24px; height: 119px; background: var(--accent-orange); }
  .accent--right-blue { left: 1174px; top: 0; width: 26px; height: 240px; background: var(--brand-blue); }
  .accent--foot-light { left: 1081px; top: 2175px; width: 119px; height: 27px; background: var(--soft-blue); }
  .accent--foot-dark { left: 964px; top: 2202px; width: 236px; height: 36px; background: var(--brand-blue); }

  .hero-illustration {
    position: absolute; left: 79px; top: 81px; width: 491px; height: 553px;
    border-radius: 245px 245px 0 0;
    background: linear-gradient(180deg, var(--pale-blue) 0%, #c5cff0 55%, #5a63cf 100%);
  }

  .brand { position: absolute; left: 930px; top: 52px; display: flex; align-items: center; gap: 10px; }
  .brand__dot { width: 40px; height: 40px; border-radius: 50%; background: var(--brand-blue); }
  .brand__name { font-size: 40px; font-weight: 700; color: var(--brand-blue); line-height: 1; }

  .headline { position: absolute; left: 593px; top: 225px; line-height: 1; }
  .headline__lead { display: block; font-size: 76px; font-weight: 500; color: var(--accent-orange); }
  .headline__main { display: block; font-size: 92px; font-weight: 900; color: var(--brand-blue); line-height: 0.95; margin-top: 4px; letter-spacing: 1px; }
  .headline__rule { position: absolute; left: 590px; top: 488px; width: 610px; height: 6px; background: var(--brand-blue); }

  .symptom-panel { position: absolute; left: 0; top: 632px; width: 591px; height: 1606px; background: var(--brand-blue); }
  .symptom-panel__rule { position: absolute; left: 79px; top: 67px; width: 512px; height: 2px; background: var(--panel-rule); }

  .chart { position: absolute; left: 0; top: 632px; width: 1176px; }
  .chart__head, .chart__row { display: grid; grid-template-columns: 591px 216px 157px 212px; }
  .chart__head { height: 68px; }
  .chart__row { height: 104.14px; }
  .chart__symptom-title { color: var(--white); font-size: 40px; font-weight: 700; text-align: right; padding-right: 103px; line-height: 68px; }
  .chart__condition { font-size: 36px; font-weight: 500; text-align: center; line-height: 70px; border-top: 2px solid var(--rule); border-bottom: 2px solid var(--rule); }
  .chart__label { position: relative; color: var(--white); font-size: 42px; font-weight: 500; text-align: right; padding-right: 103px; line-height: 104px; }
  .chart__icon {
    position: absolute; right: -55px; top: 2px; width: 100px; height: 100px; border-radius: 50%;
    border: 4px solid var(--pale-blue); z-index: 2;
    background: radial-gradient(circle at 50% 40%, #ffffff 0%, #dfe6f6 60%, #4a55d0 100%);
  }
  .chart__cell { display: flex; align-items: center; justify-content: center; font-size: 23px; font-weight: 500; border-bottom: 2px solid var(--rule); }
  .chart__cell--sub, .chart__condition--sub { border-left: 2px solid var(--rule); }
  .chart__tick { font-size: 46px; font-weight: 800; }
</style>
</head>
<body>
<main class="infographic">
  <div class="accent accent--left-blue"></div>
  <div class="accent accent--left-orange"></div>
  <div class="accent accent--right-orange"></div>
  <div class="accent accent--right-blue"></div>

  <div class="hero-illustration" role="img" aria-label="Illustration of a woman wrapped in a blanket with a scarf and a thermometer, holding a tissue box, looking unwell"></div>

  <div class="brand"><span class="brand__dot"></span><span class="brand__name">Tovipharm</span></div>

  <h1 class="headline">
    <span class="headline__lead">Do i have</span>
    <span class="headline__main">coronavirus,</span>
    <span class="headline__main">flu or cold?</span>
  </h1>
  <div class="headline__rule"></div>

  <div class="symptom-panel"><div class="symptom-panel__rule"></div></div>

  <section class="chart">
    <div class="chart__head">
      <div class="chart__symptom-title">Symptom</div>
      <div class="chart__condition">Coronavirus</div>
      <div class="chart__condition chart__condition--sub">Flu</div>
      <div class="chart__condition chart__condition--sub">Cold</div>
    </div>

    <div class="chart__row">
      <div class="chart__label">Incubation Period<span class="chart__icon" role="img" aria-label="Clock icon"></span></div>
      <div class="chart__cell">1 - 14 days</div><div class="chart__cell chart__cell--sub">1 - 4 days</div><div class="chart__cell chart__cell--sub">1 - 3 days</div>
    </div>
    <div class="chart__row">
      <div class="chart__label">Symptom onset<span class="chart__icon" role="img" aria-label="Icon of a person feeling sudden illness"></span></div>
      <div class="chart__cell">Gradual</div><div class="chart__cell chart__cell--sub">Abrupt</div><div class="chart__cell chart__cell--sub">Gradual</div>
    </div>
    <div class="chart__row">
      <div class="chart__label">Fever<span class="chart__icon" role="img" aria-label="Icon of a person with a thermometer"></span></div>
      <div class="chart__cell"><span class="chart__tick">√</span></div><div class="chart__cell chart__cell--sub"><span class="chart__tick">√</span></div><div class="chart__cell chart__cell--sub">Rare</div>
    </div>
    <div class="chart__row">
      <div class="chart__label">Cough<span class="chart__icon" role="img" aria-label="Icon of a person coughing"></span></div>
      <div class="chart__cell"><span class="chart__tick">√</span></div><div class="chart__cell chart__cell--sub"><span class="chart__tick">√</span></div><div class="chart__cell chart__cell--sub">Mild to moderate</div>
    </div>
    <div class="chart__row">
      <div class="chart__label">Fatigue<span class="chart__icon" role="img" aria-label="Icon of a tired person"></span></div>
      <div class="chart__cell"><span class="chart__tick">√</span></div><div class="chart__cell chart__cell--sub"><span class="chart__tick">√</span></div><div class="chart__cell chart__cell--sub">Sometimes</div>
    </div>
    <div class="chart__row">
      <div class="chart__label">Runny nose<span class="chart__icon" role="img" aria-label="Icon of a person with a runny nose"></span></div>
      <div class="chart__cell">Sometimes</div><div class="chart__cell chart__cell--sub">Sometimes</div><div class="chart__cell chart__cell--sub"><span class="chart__tick">√</span></div>
    </div>
    <div class="chart__row">
      <div class="chart__label">Nasal congestion<span class="chart__icon" role="img" aria-label="Icon of a person with a blocked nose"></span></div>
      <div class="chart__cell">Sometimes</div><div class="chart__cell chart__cell--sub">Sometimes</div><div class="chart__cell chart__cell--sub"><span class="chart__tick">√</span></div>
    </div>
    <div class="chart__row">
      <div class="chart__label">Diarrhea<span class="chart__icon" role="img" aria-label="Icon of a person with stomach upset"></span></div>
      <div class="chart__cell">Sometimes</div><div class="chart__cell chart__cell--sub">Sometimes</div><div class="chart__cell chart__cell--sub">Rare</div>
    </div>
    <div class="chart__row">
      <div class="chart__label">Body aches<span class="chart__icon" role="img" aria-label="Icon of a person with aching body"></span></div>
      <div class="chart__cell">Sometimes</div><div class="chart__cell chart__cell--sub"><span class="chart__tick">√</span></div><div class="chart__cell chart__cell--sub">Slight</div>
    </div>
    <div class="chart__row">
      <div class="chart__label">Sore throat<span class="chart__icon" role="img" aria-label="Icon of a person with a sore throat"></span></div>
      <div class="chart__cell">Sometimes</div><div class="chart__cell chart__cell--sub">Sometimes</div><div class="chart__cell chart__cell--sub"><span class="chart__tick">√</span></div>
    </div>
    <div class="chart__row">
      <div class="chart__label">Headache<span class="chart__icon" role="img" aria-label="Icon of a person with a headache"></span></div>
      <div class="chart__cell">Sometimes</div><div class="chart__cell chart__cell--sub"><span class="chart__tick">√</span></div><div class="chart__cell chart__cell--sub">Rare</div>
    </div>
    <div class="chart__row">
      <div class="chart__label">Loss of appetite<span class="chart__icon" role="img" aria-label="Icon of a person with no appetite"></span></div>
      <div class="chart__cell">Sometimes</div><div class="chart__cell chart__cell--sub"><span class="chart__tick">√</span></div><div class="chart__cell chart__cell--sub">Sometimes</div>
    </div>
    <div class="chart__row">
      <div class="chart__label">Shortness of breat<span class="chart__icon" role="img" aria-label="Icon of a person short of breath"></span></div>
      <div class="chart__cell"><span class="chart__tick">√</span></div><div class="chart__cell chart__cell--sub">Sometimes</div><div class="chart__cell chart__cell--sub">Mild</div>
    </div>
    <div class="chart__row">
      <div class="chart__label">Repiratory issues<span class="chart__icon" role="img" aria-label="Icon of a person with breathing problems"></span></div>
      <div class="chart__cell"><span class="chart__tick">√</span></div><div class="chart__cell chart__cell--sub">Sometimes</div><div class="chart__cell chart__cell--sub">Sometimes</div>
    </div>
  </section>

  <div class="accent accent--foot-light"></div>
  <div class="accent accent--foot-dark"></div>
</main>
</body>
</html>
```